Qivora IT Company Business Card

📌 Objective:
Create a modern, fluid and stylish business card that reflects the identity of our IT company and our partnership with Veltrana.
📍 Key information:
• Company name: Qivora
• Activity: Veltrana 720 Expert
• Colors to favor: Inspired by the Qivora logo
• Style: Minimalist, modern, professional
• Front / Back:
• Items to include:
o Company logo
o Name and surname
o Post
o Email
o Phone
o Website
o QR code (optional)
🎨 Inspirations & Expectations:
• Sleek design with a high-tech touch
• Possibly subtle graphic elements linked to the Veltrana universe
• Good readability and balance between text and visuals

Lent pour commenter

Target Market(s)

Private, public

Contact Information for Business Card

Veltrana720, Formation, Gouvernance, Migration, Sécurité

Colors
6B429C
8869AF
B7A5CE
E3DAEB
F3F0F8

Requirements
Nice to have
• Have the icons of the applications I work on

```html
<!DOCTYPE html>
<html lang="en">
<head>
<meta charset="utf-8">
<title>Qivora Business Card</title>
<link rel="stylesheet" href="https://fonts.googleapis.com/css2?family=Montserrat:wght@400;500;600;700&display=swap">
<style>
  :root {
    --stage: #2b2b2b;
    --card-dark: #323232;
    --card-light: #ffffff;
    --ink: #111111;
    --white: #ffffff;
    --accent-orange: #f0642f;
    --accent-blue: #1f6fd1;
    --accent-cyan: #2ab3c9;
    --accent-pink: #e9226d;
    --accent-purple: #9b3cf5;
    --muted: #cfcfcf;
  }
  * { box-sizing: border-box; margin: 0; padding: 0; }
  html, body {
    width: 1200px; height: 689px; overflow: hidden;
    background: var(--stage);
    font-family: "Montserrat", sans-serif;
  }
  .stage {
    position: relative; width: 1200px; height: 689px;
    display: flex; align-items: center; justify-content: center; gap: 60px;
  }
  .card {
    position: relative; width: 520px; height: 297px;
    border-radius: 18px; overflow: hidden;
  }
  .card--front {
    background: var(--card-dark);
    display: flex; align-items: center; justify-content: center;
  }
  .wordmark {
    display: flex; align-items: center; gap: 14px;
    font-weight: 600; letter-spacing: -1px;
  }
  .wordmark__dot {
    border-radius: 50%; background: var(--accent-orange); flex: none;
  }
  .card--front .wordmark { color: var(--white); font-size: 68px; }
  .card--front .wordmark__dot { width: 30px; height: 30px; }

  .card--back { background: var(--card-dark); }
  .back__top {
    position: absolute; left: 0; top: 0; width: 100%; height: 170px;
    background: var(--card-light);
    display: flex; align-items: center; justify-content: center;
  }
  .card--back .wordmark { color: var(--ink); font-size: 50px; }
  .card--back .wordmark__dot { width: 22px; height: 22px; }
  .spectrum-line {
    position: absolute; left: 0; top: 170px; width: 100%; height: 4px;
    background: linear-gradient(90deg,
      var(--accent-blue) 0%, var(--accent-cyan) 38%,
      var(--accent-pink) 39%, var(--accent-orange) 76%,
      var(--accent-purple) 77%, var(--accent-purple) 100%);
  }
  .back__details {
    position: absolute; left: 0; top: 174px; width: 100%; height: 123px;
    display: flex; align-items: center; justify-content: center; gap: 18px;
  }
  .person { text-align: right; }
  .person__name {
    color: var(--white); font-weight: 600; font-size: 19px; letter-spacing: 0.5px;
  }
  .person__role {
    color: var(--accent-orange); font-size: 12px; font-weight: 500; margin-top: 2px;
  }
  .divider { width: 1px; height: 48px; background: var(--muted); opacity: 0.6; }
  .contact { list-style: none; }
  .contact__item {
    display: flex; align-items: center; gap: 8px;
    color: var(--white); font-size: 12px; line-height: 17px;
  }
  .contact__icon { width: 11px; height: 11px; flex: none; fill: var(--accent-orange); }
</style>
</head>
<body>
<main class="stage">
  <section class="card card--front" aria-label="Card front">
    <div class="wordmark"><span class="wordmark__dot"></span><span>Qivora</span></div>
  </section>

  <section class="card card--back" aria-label="Card back">
    <div class="back__top">
      <div class="wordmark"><span class="wordmark__dot"></span><span>Qivora</span></div>
    </div>
    <div class="spectrum-line"></div>
    <div class="back__details">
      <div class="person">
        <p class="person__name">NOAH BERGEN</p>
        <p class="person__role">President</p>
      </div>
      <div class="divider"></div>
      <ul class="contact">
        <li class="contact__item">
          <svg class="contact__icon" viewBox="0 0 24 24"><path d="M6.6 10.8a15.2 15.2 0 0 0 6.6 6.6l2.2-2.2a1 1 0 0 1 1-.25 11.4 11.4 0 0 0 3.6.57 1 1 0 0 1 1 1V20a1 1 0 0 1-1 1A17 17 0 0 1 3 4a1 1 0 0 1 1-1h3.5a1 1 0 0 1 1 1c0 1.25.2 2.45.57 3.57a1 1 0 0 1-.25 1z"/></svg>
          <span>555-204-7781</span>
        </li>
        <li class="contact__item">
          <svg class="contact__icon" viewBox="0 0 24 24"><path d="M2 5h20v14H2z M3.5 6.5 12 13l8.5-6.5" stroke="#323232" stroke-width="1.6"/></svg>
          <span>info@qivora.com</span>
        </li>
        <li class="contact__item">
          <svg class="contact__icon" viewBox="0 0 24 24"><circle cx="12" cy="12" r="10"/><path d="M2 12h20M12 2c3 3 3 17 0 20M12 2c-3 3-3 17 0 20" stroke="#323232" stroke-width="1.5" fill="none"/></svg>
          <span>www.qivora.com</span>
        </li>
      </ul>
    </div>
  </section>
</main>
</body>
</html>
```